Letterhead & Business Card for our Professional Practice (Financial Services)

We are looking for someone to design a letterhead and business card for our business, which is a professional practice called Harbor Lumen Capital Limited. The website is at www.harborrlumencapital.example.co.uk.

The letterhead needs to have: (a) our logo (b) address (c) telephone number (d) email address and (e) our company number.

We would like the stationary to be consistent with the website.

I have attached the logo in EPS and PNG format.

Target Market(s)

Professional services, large commercial enterprises, financial services

Industry/Entity Type

Financial Service

Font styles to use
Serif

Colors
3176b5
f04a50

Requirements
Must have
• Be consistent with our website located at www.harborlumencapital.example.co.uk
• Be in the following formats:
• 1. Word template for the letterhead
• 2. PDF for the letterhead with setup and bleeds required at www.presskite.example.co.uk
• 3. PDF for the business card with setup and bleeds required at www.presskite.example.co.uk
Nice to have
• Something with a really interesting design that says "these guys are professional but dynamic and interesting"
Should not have
• Boring

```html
<!DOCTYPE html>
<html lang="en">
<head>
<meta charset="utf-8">
<title>Harbor Lumen Capital – Business Card</title>
<link rel="stylesheet" href="https://fonts.googleapis.com/css2?family=Marcellus&family=Exo+2:wght@300&display=swap">
<style>
  :root {
    --brand-blue: #032a94;
    --brand-red: #d4000f;
    --paper: #ffffff;
    --frame: #111111;
    --page: #ffffff;
  }
  html, body {
    margin: 0;
    padding: 0;
    width: 1200px;
    height: 757px;
    overflow: hidden;
    background: var(--page);
  }
  .business-card {
    display: block;
    width: 1200px;
    height: 757px;
  }
  .card-base { fill: var(--paper); stroke: var(--frame); stroke-width: 1.5; }
  .top-band, .wave-blue, .phone-tab, .phone-field { fill: var(--brand-blue); }
  .wave-red, .brand-square { fill: var(--brand-red); }
  .phone-field { stroke: var(--paper); stroke-width: 1.2; }
  .icon-tab { fill: var(--paper); }
  .icon-red { fill: var(--brand-red); }
  .icon-red-line { fill: none; stroke: var(--brand-red); stroke-width: 2.6; stroke-linejoin: round; }
  .icon-white { fill: var(--paper); }
  .company-name {
    font-family: "Marcellus", serif;
    font-size: 63px;
    fill: var(--brand-blue);
  }
  .phone-number {
    font-family: "Exo 2", sans-serif;
    font-weight: 300;
    font-size: 42px;
    letter-spacing: 1.5px;
    fill: var(--paper);
  }
  .contact-line {
    font-family: "Exo 2", sans-serif;
    font-weight: 300;
    font-size: 29px;
    fill: var(--paper);
  }
</style>
</head>
<body>
<svg class="business-card" viewBox="0 0 1160 732" xmlns="http://www.w3.org/2000/svg" role="img" aria-label="Harbor Lumen Capital business card">
  <defs>
    <clipPath id="card-clip">
      <rect x="33" y="40" width="1087" height="638"/>
    </clipPath>
  </defs>

  <rect class="card-base" x="33" y="40" width="1087" height="638"/>

  <g clip-path="url(#card-clip)">
    <rect class="top-band" x="33" y="40" width="1087" height="12"/>

    <!-- Brand block -->
    <rect class="brand-square" x="288" y="82" width="187" height="187"/>
    <text class="company-name" x="85" y="355">Harbor Lumen Capital</text>

    <!-- Phone -->
    <rect class="phone-tab" x="703" y="125" width="82" height="75" rx="10"/>
    <rect class="phone-field" x="772" y="125" width="370" height="75" rx="12"/>
    <path class="icon-white" d="M727 140 c4-3 8-2 9 2 l4 11 c1 3 0 5-3 6 l-3 2 c2 8 5 13 10 19 l3-2 c2-2 5-2 7 0 l6 8 c2 3 1 6-2 8 l-4 3 c-5 3-12 0-17-7 c-8-11-13-24-14-37 c0-6 1-11 4-13z"/>
    <text class="phone-number" x="798" y="175">01632 960418</text>

    <!-- Waves -->
    <path class="wave-red" d="M33 428 C200 406 400 414 560 440 C760 470 960 520 1120 558 L1120 632 C950 575 760 505 560 455 C420 424 200 420 33 440 Z"/>
    <path class="wave-blue" d="M33 452 C200 426 420 428 560 462 C760 512 950 585 1120 642 L1120 678 L33 678 Z"/>

    <!-- Email -->
    <rect class="icon-tab" x="20" y="483" width="100" height="47" rx="8"/>
    <rect class="icon-red-line" x="75" y="497" width="31" height="20" rx="2"/>
    <path class="icon-red-line" d="M75 498 L90.5 510 L106 498"/>
    <text class="contact-line" x="157" y="518">contact@harborlumencapital.example.co.uk</text>

    <!-- Address -->
    <rect class="icon-tab" x="20" y="557" width="100" height="47" rx="8"/>
    <path class="icon-red" d="M91 600 C84 589 79 581 79 575 a12 12 0 0 1 24 0 c0 6-5 14-12 25z"/>
    <circle class="icon-tab" cx="91" cy="574" r="4.5"/>
    <text class="contact-line" x="154" y="588">14-15 Quayside Row</text>
    <text class="contact-line" x="154" y="628">Eastmere, Berkshire, EM2 7QA.</text>
  </g>
</svg>
</body>
</html>
```